Passport Brochure

We are a start-up training and staffing company called Verlow Consulting. We assist people in getting work in the Financial Industry.
We need a brochure for our new "Career Beacon Program".
We've put together a mock up of what we are looking for but we need someone to put a more professional touch on it, see "Creative Brief" attached obviously the pictures are just examples to give an idea.
The 4 slides will be printed with each slide being 3.5 x 5 inches gloss brochure.
We want the front page to have the picture shown or very similar.
The middle of the brochure should look like the center-fold of a passport slide 2 should be the left page of a passport and slide 3 would be the right side of a passport and have an approved symbol
Slide 3 should have an integrated picture of the Marrowby Building
The back should look like the back of a passport and contain our logo, attached.

Hello and Thank you all for your great designs. Can everyone please ensure that all pages(front and back) within each design are added to the same submission. Thanks, Darius

```html
<!DOCTYPE html>
<html lang="en">
<head>
<meta charset="utf-8">
<title>The Verlow Career Beacon Program</title>
<link href="https://fonts.googleapis.com/css2?family=Tinos:wght@400;700&display=swap" rel="stylesheet">
<style>
  :root {
    --paper: #fdd89b;
    --plum: #862a52;
    --ink: #7a2547;
    --sky-top: #a9c3e6;
    --sky-low: #c9d8ec;
    --tower: #5b6f8c;
  }
  * { margin: 0; padding: 0; box-sizing: border-box; }
  html, body { width: 840px; height: 1200px; overflow: hidden; }
  body {
    background: var(--paper);
    font-family: "Tinos", "Times New Roman", serif;
    color: var(--ink);
    position: relative;
  }
  .corner-tab {
    position: absolute; left: 688px; top: 0;
    width: 118px; height: 228px;
    background: var(--plum);
    border-radius: 0 0 59px 59px;
  }
  .title {
    position: absolute; left: 40px; width: 640px; top: 100px;
    text-align: right; font-weight: 700; color: var(--plum); line-height: 1;
  }
  .title .lead { display: block; font-size: 40px; }
  .title .main { display: block; font-size: 62px; letter-spacing: 0.5px; }
  .section-head {
    position: absolute; left: 0; width: 840px; top: 252px;
    text-align: center; font-size: 31px; font-weight: 700; color: var(--plum);
  }
  .overview {
    position: absolute; left: 24px; top: 318px;
    width: 788px; height: 846px;
    border: 3px solid var(--plum); border-radius: 28px;
  }
  .features {
    position: absolute; left: 46px; width: 736px; top: 354px;
    list-style: none; font-size: 26px; line-height: 32px; letter-spacing: 1px;
  }
  .features li { margin-bottom: 12px; text-align: justify; }
  .details {
    position: absolute; left: 46px; width: 440px; top: 668px;
    font-size: 26px; line-height: 32px; letter-spacing: 1px;
  }
  .details p { margin-bottom: 16px; }
  .details .voucher { margin-bottom: 14px; }
  .details .label { text-decoration: underline; text-underline-offset: 4px; text-decoration-thickness: 1px; }
  .details .code { font-weight: 700; letter-spacing: 1.5px; }
  .details .location { margin-bottom: 0; }
  .tower-photo {
    position: absolute; left: 494px; top: 746px;
    width: 304px; height: 404px;
    border: 3px solid var(--plum); border-radius: 24px;
    background: linear-gradient(180deg, var(--sky-top) 0%, var(--sky-low) 45%, var(--tower) 100%);
  }
</style>
</head>
<body>
  <div class="corner-tab"></div>

  <h1 class="title">
    <span class="lead">THE VERLOW CAREER</span>
    <span class="main">BEACON PROGRAM</span>
  </h1>

  <h2 class="section-head">PROGRAM OVERVIEW</h2>

  <div class="overview"></div>

  <ul class="features">
    <li>– One Day Financial Training Crash Course, delivered by Financial Professionals. <b>(Worth £965)</b></li>
    <li>– One to One Interview Training with a Financial Professional. <b>(Worth £125)</b></li>
    <li>– CV Review with Experienced Recruitment Consultant. <b>(Worth £45)</b></li>
    <li>– Entry into Work Experience Programme.</li>
    <li>– Individual assistance with the Lantern Recruitment Consultant</li>
  </ul>

  <div class="details">
    <p><span class="label">Total Value</span> – <b>£1135</b></p>
    <p class="voucher"><span class="label">Voucher Code 20% OFF</span> – <span class="code">CBPAPR24</span></p>
    <p class="location"><span class="label">Location</span> –<br>
      Applicants will attend training in<br>our offices at <b>Level 30,</b><br><b>Marrowby Building.</b></p>
  </div>

  <div class="tower-photo" role="img" aria-label="Photo of the Marrowby Building, a tall glass tower in the city skyline under a pale blue sky"></div>
</body>
</html>
```